Broschüre für Gleichstellungsstelle einer kommunalen Stadtverwaltung
Zielgruppe
Wir sind die Gleichstellungsstelle einer kommunalen Stadtverwaltung (Einwohner*innen ca. 74.500) und richten uns mit unserer Arbeit grundsätzlich an alle Menschen.
Wir wollen eine Broschüre zum Handlungsleitfaden für die geschlechtergerechte Sprache bei der Stadt erstellen. Dieser soll an die Beschäftigten als Unterstützung verteilt werden.
Aufgabenstellung
- Broschüre mit Wire-O-Bindung, Druckformat 14,8 cm x 14,8 cm, Endformat 15,0 x 15,0 cm
- Spiralbindung an der Kopfseite
- doppelseitiges Deckblatt und Rückseite
- 16 Seiten Inhalt, wobei lediglich die Vorderseiten Text enthalten
- Schriftart (optimal Avenir Next, alternativ Arial) und Farbschema laut Corporate Design
- Der Text ist vorgegeben, die Gestaltung ist im Rahmen des Corporate Designs frei
Es soll eine ansprechende Broschüre gestaltet werden, welche die Leser*innen zum Blättern einlädt. Das bedeutet, dass alle Seiten (Deckblatt, Inhaltsseiten und Rückseiten) bei der Gestaltung berücksichtigt werden müssen.
Am Ende soll neben den üblichen Dateien auch eine fertige Druckdatei (siehe Datenblatt) zur Verfügung gestellt werden. Dabei ist zu beachten, dass die Spiralbindung des fertigen Produkts an der Kopfseite sein soll.

```html
<!DOCTYPE html>
<html lang="de">
<head>
<meta charset="utf-8">
<title>Anträge und Formulare</title>
<link rel="stylesheet" href="https://fonts.googleapis.com/css2?family=Nunito+Sans:wght@400;600;700;800&display=swap">
<style>
  :root {
    --band: #01514a;
    --band-text: #ffffff;
    --band-highlight: #c5cecb;
    --accent: #2f6f69;
    --text: #5b5b5b;
    --page: #ffffff;
    --frame: #d6d6d6;
  }
  * { margin: 0; padding: 0; box-sizing: border-box; }
  html, body { width: 1200px; height: 1200px; overflow: hidden; background: var(--page); }
  body { font-family: "Nunito Sans", "Avenir Next", Arial, sans-serif; color: var(--text); }
  .page { position: relative; width: 1200px; height: 1200px; border: 2px solid var(--frame); }
  .intro-band {
    position: absolute; left: 0; top: 0; width: 100%; height: 383px;
    background: var(--band); color: var(--band-text); padding: 128px 81px 0;
  }
  .intro-title { font-size: 38px; font-weight: 800; letter-spacing: 0.2px; line-height: 1.1; margin-bottom: 10px; }
  .intro-text { font-size: 28px; line-height: 40px; font-weight: 400; }
  .intro-text strong { color: var(--band-highlight); font-weight: 700; }
  .section-heading { color: var(--accent); font-weight: 700; font-size: 36px; line-height: 1.2; }
  .block { position: absolute; left: 81px; right: 60px; }
  .pair { display: grid; grid-template-columns: 405px 1fr; font-size: 27px; line-height: 39.5px; }
  .forms { top: 440px; }
  .forms .pair { margin-top: 2px; }
  .note { top: 683px; font-size: 27px; line-height: 39.5px; }
  .compare { top: 842px; }
  .compare .section-heading { font-size: 35px; }
  .compare .col-right { line-height: 40.5px; }
</style>
</head>
<body>
<main class="page">
  <header class="intro-band">
    <h1 class="intro-title">ANTRÄGE UND FORMULARE</h1>
    <p class="intro-text">Der gesetzliche Auftrag umfasst auch die <strong>geschlechtergerechte Ansprache</strong> im gesamten Publikumsverkehr in der Verwaltung. Manche Situation lässt sich bei der Formulierung durch die persönliche Ansprache oder das Gendersternchen lösen. Zum Beispiel:</p>
  </header>

  <section class="block forms">
    <h2 class="section-heading">Beide Formen sind möglich:</h2>
    <div class="pair">
      <div class="col-left">(Ihr) Name<br>(Ihre) Unterschrift<br>verfasst von</div>
      <div class="col-right">Name Antragssteller*in<br>Unterschrift Antragssteller*in<br>Verfasser*in</div>
    </div>
  </section>

  <p class="block note">Es gibt aber auch Wörter, die eine feststehende juristische Definition<br>tragen und somit (bislang) nicht verändert werden dürfen. Diese<br>Begriffe können Sie jedoch beschreibend verwenden. Zum Beispiel:</p>

  <section class="block compare">
    <div class="pair">
      <div class="col-left">
        <h2 class="section-heading">statt:</h2>
        Gesetzlicher Vertreter<br>Gesetzlicher Betreuer
      </div>
      <div class="col-right">
        <h2 class="section-heading">besser:</h2>
        gesetzlich vertreten durch / Vertretung durch<br>gesetzlich betreut durch / gesetzliche<br>Betreuung durch
      </div>
    </div>
  </section>
</main>
</body>
</html>
```